CREATE A 2 layout and logo ( velunarix )

I need to create 2 layout for my company being a homepage will be like and other client control panel and need to create the logo of the company, my company works with website hosting and sale of dedicated server and VPS cloud the company name and velunarix, I want the site to be very accessible and that is not too flashy

Target Market(s)

website hosting

Industry/Entity Type

It Company

Number of Pages Required

2 page

Font styles to use
Sans Serif

Requirements
Must have
• domain velunarix.example
Nice to have
• banners, login area, login webmail
Should not have
• no preference

```html
<!DOCTYPE html>
<html lang="en">
<head>
<meta charset="utf-8">
<title>velunarix.example — Domains &amp; Hosting</title>
<link rel="stylesheet" href="https://fonts.googleapis.com/css2?family=Source+Sans+3:ital,wght@0,400;0,600;0,700;1,600&family=Arimo:wght@400&display=swap">
<style>
  :root{
    --orange:#ff6a00;
    --navy:#003d73;
    --navy-deep:#002a52;
    --ink:#4a4a4a;
    --muted:#555;
    --card:#f1f1f1;
    --card-line:#bdbdbd;
    --white:#fff;
    --black:#0d0d0d;
  }
  *{box-sizing:border-box;margin:0;padding:0}
  html,body{width:999px;height:1200px;overflow:hidden;background:var(--white)}
  body{position:relative;font-family:"Source Sans 3",sans-serif;color:var(--ink)}
  .abs{position:absolute}

  .brand{font-family:"Source Sans 3",sans-serif;font-weight:700;color:var(--ink);letter-spacing:.3px}
  .header-brand{left:28px;top:30px;font-size:34px}

  .btn{position:absolute;display:flex;align-items:center;justify-content:center;border-radius:9px;color:var(--white);font-size:15px}
  .btn-orange{background:var(--orange)}
  .btn-navy{background:var(--navy)}

  .search{left:665px;top:33px;width:314px;height:55px;background:var(--navy);border-radius:9px}
  .search-field{left:15px;top:12px;width:237px;height:30px;background:var(--white);font-style:italic;font-weight:600;color:#aaa;font-size:17px;padding:3px 14px}
  .search-go{right:0;top:0;width:48px;height:55px;background:var(--orange);border-radius:0 9px 9px 0;display:flex;align-items:center;justify-content:center}

  .main-nav{left:0;top:110px;width:999px;height:28px;background:var(--orange);display:flex;justify-content:center;align-items:center;gap:22px;color:var(--white);font-size:12.5px}
  .main-nav .sep{opacity:.9}

  .hero-art{left:0;top:180px;width:657px;height:400px;background:linear-gradient(180deg,#d9dde2 0%,#b7bfc9 45%,#f4f6f8 100%)}
  .hero-title{right:20px;top:182px;text-align:right;color:var(--navy);font-size:40px;line-height:48px}
  .hero-rule{left:620px;top:293px;width:364px;height:1px;background:var(--orange)}
  .hero-text{right:20px;top:306px;width:330px;text-align:right;font-size:17.5px;line-height:22px;color:var(--muted)}

  .finder{left:395px;top:460px;width:604px;height:120px;background:var(--navy)}
  .finder-field{position:absolute;width:237px;height:30px;background:var(--white);font-style:italic;font-weight:600;color:#aaa;font-size:17px;padding:3px 14px}
  .finder-go{position:absolute;left:518px;top:66px;width:61px;height:36px;background:var(--orange);border-radius:7px;display:flex;align-items:center;justify-content:center}

  .band{left:0;top:580px;width:999px;height:27px;background:var(--orange)}

  .card{position:absolute;top:648px;width:314px;height:289px;background:var(--card);border:1px solid var(--card-line)}
  .card-title{position:absolute;left:11px;top:8px;width:290px;height:42px;background:var(--ink);color:var(--white);font-size:29px;display:flex;align-items:center;justify-content:center}
  .card-line{position:absolute;left:11px;width:290px;height:1px;background:#dcdcdc}
  .card-art{position:absolute;left:11px;top:83px;width:138px;height:127px}
  .card-text{position:absolute;left:159px;top:79px;width:145px;font-size:13.5px;line-height:17px;color:var(--ink)}
  .card-btn{position:absolute;left:95px;top:244px;width:125px;height:26px;background:var(--orange);border-radius:13px;color:var(--white);font-size:12px;display:flex;align-items:center;justify-content:center}

  .site-footer{left:0;top:974px;width:999px;height:176px;background:linear-gradient(180deg,#003e78 0%,#002a52 100%)}
  .footer-col{position:absolute;top:30px;width:169px;color:var(--white)}
  .footer-col h3{font-weight:400;font-size:20px;padding-bottom:8px;border-bottom:1px solid #6f94bb;margin-bottom:14px}
  .footer-col li{list-style:none;font-family:"Arimo",sans-serif;font-size:14px;line-height:26.5px}

  .bottom-bar{left:0;top:1150px;width:999px;height:50px;background:var(--black);color:#ccc}
  .bottom-brand{left:25px;top:12px;font-size:21px;color:#bbb}
  .bottom-nav{left:315px;top:0;height:50px;display:flex;align-items:center;gap:32px;font-family:"Arimo",sans-serif;font-size:12.5px}
  .social{top:12px;width:26px;height:26px;border-radius:50%;background:var(--orange)}
</style>
</head>
<body>

<header>
  <div class="abs brand header-brand">velunarix.example</div>
  <div class="btn btn-orange" style="left:481px;top:42px;width:78px;height:36px">Login</div>
  <div class="btn btn-navy" style="left:569px;top:42px;width:78px;height:36px">Sign up</div>
  <div class="abs search">
    <div class="abs search-field">search</div>
    <div class="abs search-go">
      <svg width="26" height="26" viewBox="0 0 26 26"><circle cx="15" cy="11" r="7.5" fill="none" stroke="#fff" stroke-width="3"/><line x1="9.5" y1="16.5" x2="3.5" y2="22.5" stroke="#fff" stroke-width="3.5" stroke-linecap="round"/></svg>
    </div>
  </div>
</header>

<nav class="abs main-nav">
  <span>HOME</span><span class="sep">|</span><span>ABOUT</span><span class="sep">|</span><span>HOSTING</span><span class="sep">|</span><span>DOMAINS</span><span class="sep">|</span><span>CONTACT</span>
</nav>

<section class="hero">
  <div class="abs hero-art" role="img" aria-label="Row of silver server towers with glowing blue bays"></div>
  <h1 class="abs hero-title" style="font-weight:400">Domains &amp; Hosting<br>Packages made easy.</h1>
  <div class="abs hero-rule"></div>
  <p class="abs hero-text">Lorem ipsum dolor sit amet consectetur adipiscing elit lorem ipsum dolor sit amet consectetur adipiscing elit.</p>
  <div class="btn btn-orange" style="left:751px;top:395px;width:108px;height:36px">Learn More</div>
  <div class="btn btn-navy" style="left:869px;top:395px;width:109px;height:36px">BUY now</div>

  <form class="abs finder">
    <div class="finder-field" style="left:25px;top:24px">City, State</div>
    <div class="finder-field" style="left:275px;top:24px">Country</div>
    <div class="finder-field" style="left:25px;top:70px">domain type</div>
    <div class="finder-field" style="left:275px;top:70px">Hosting package</div>
    <div class="finder-go">
      <svg width="26" height="26" viewBox="0 0 26 26"><circle cx="15" cy="11" r="7.5" fill="none" stroke="#fff" stroke-width="3"/><line x1="9.5" y1="16.5" x2="3.5" y2="22.5" stroke="#fff" stroke-width="3.5" stroke-linecap="round"/></svg>
    </div>
  </form>
</section>

<div class="abs band"></div>

<section class="services">
  <article class="card" style="left:17px">
    <h2 class="card-title" style="font-weight:400">Dedicated Servers</h2>
    <div class="card-line" style="top:66px"></div>
    <div class="card-art" role="img" aria-label="Close view of rack-mounted servers" style="background:linear-gradient(135deg,#1c2230,#5a6478 55%,#0c0f16)"></div>
    <p class="card-text">lorem ipsum dolor sit amet consectetur und adipiscing elit sit amet lorem ipsum dolor sit amet consectetur und elit sit amet ipsum sit elit. ipsum lorem</p>
    <div class="card-line" style="top:228px"></div>
    <div class="card-btn">VIEW DETAILS</div>
  </article>
  <article class="card" style="left:342px">
    <h2 class="card-title" style="font-weight:400">Domain Names</h2>
    <div class="card-line" style="top:66px"></div>
    <div class="card-art" role="img" aria-label="Globe linked to several laptops" style="background:linear-gradient(180deg,#e9edf1,#9ebdd6 50%,#f2f2f2)"></div>
    <p class="card-text">lorem ipsum dolor sit amet consectetur und adipiscing elit sit amet lorem ipsum dolor sit amet consectetur und adipiscing elit sit amet sit consectetur elit.</p>
    <div class="card-line" style="top:228px"></div>
    <div class="card-btn">VIEW DETAILS</div>
  </article>
  <article class="card" style="left:666px">
    <h2 class="card-title" style="font-weight:400">Hosting Packages</h2>
    <div class="card-line" style="top:66px"></div>
    <div class="card-art" role="img" aria-label="Globe surrounded by black server towers" style="background:linear-gradient(180deg,#e6ebef,#5b86a8 45%,#2a2d33 75%,#f0f0f0)"></div>
    <p class="card-text">lorem ipsum dolor sit amet consectetur und adipiscing elit sit amet lorem ipsum dolor und adipiscing elit sit amet lorem adipiscing sit consectetur.</p>
    <div class="card-line" style="top:228px"></div>
    <div class="card-btn">VIEW DETAILS</div>
  </article>
</section>

<footer class="abs site-footer">
  <div class="footer-col" style="left:66px"><h3>About Us</h3><ul><li>General Information</li><li>Our Mission</li></ul></div>
  <div class="footer-col" style="left:306px"><h3>Hosting Packages</h3><ul><li>Adipiscing Elit</li><li>Ipsum Lorem Sit Amet</li></ul></div>
  <div class="footer-col" style="left:546px"><h3>Maintenance</h3><ul><li>Lorem ipsum</li><li>Dolor Sit Amet Consectetur</li></ul></div>
  <div class="footer-col" style="left:796px"><h3>Contact Us</h3><ul><li>Friendlane</li><li>Chirpline</li><li>Email us</li></ul></div>
</footer>

<div class="abs bottom-bar">
  <div class="abs brand bottom-brand">velunarix.example</div>
  <nav class="abs bottom-nav"><span>HOME</span><span>|</span><span>ABOUT</span><span>|</span><span>REVIEWS</span><span>|</span><span>CONTACT</span></nav>
  <div class="abs social" style="left:838px" aria-label="Friendlane"></div>
  <div class="abs social" style="left:889px" aria-label="Chirpline"></div>
  <div class="abs social" style="left:941px" aria-label="Pinboardly"></div>
</div>

</body>
</html>
```